2-sided DIN A5 flyer for Real Estate company

Please read carefully: - Flyers should be in A5, 2-sided - Design should be eye-catching but still looking serious and trustful, modern, fresh, clean - The flyer will be sent to households. On the flyer it says that people can earn money. So the flyer should be animate people to contact me and share information with me. - The text you can use is written in «text». Please use different font sizes. Fontsize indication is written in front of «text». I would like to be able to do this in the future. I would like to be able to do this. * Update afterfirst designs I received * If you use pictures, keep in mind the reader of the flyer will not sell me a house, he will sell me a contact. So it is worth the money to pay for the money. If you use money, please use swiss currency money picture! But overall the text should be in the focus, especially on front side! The logo of my company is not too important! Front side: - Logo - Eye-catching design using the color theme of logo, not just one background color, maybe different blues - The text should be in the focus and as big as possible. Play with different sizes, bold / unbold, capital letters, etc. The goal should be that the text is the first thing that the reader see. - Dont use too many pictures. If so, you can use a graphical for tip (ie light bubble) in front of a real estate, then an equal sign and then a graphical for money or incentive. Cause thats what they get. - Big-font: «Your tip is us up to CHF 3 '- Big-font:« Big-font: 500.- worth! »- Phone icon, medium-font:« 044 512 83 91 »- Mail icon, medium-font:« ch@torvald-immo.ch »- Website icon, medium-font:« www.torvald- Immo.ch »Back side: Big-font:« Your tip is worth MONEY! "Medium-font:" You know a potential real estate salesman in your family, friends, acquaintances, club or professional world? Whether immediate or in the near future your tip can pay off for you. After a successful placement we will give you a tip-and-shoot commission of up to CHF 3'500 .-- »Medium-font. «And as simple as this works: 1. You contact us and give us the willing owner 2. We contact the owner and conclude a brokerage from 3. We start the sales process and inform you about the progress 4. After you have successfully completed your sales contract, you will receive your donor commission! »Medium-font. «Example: Thanks to your tip we can sell a property to 1.5 million. Your donor commission is CHF 3'000 .-- (0.2% of CHF 1'500'000.-) »Medium-font. "Torvald Immobilien Treuhand AG Almweg 14 6331 Hünenberg" - Phone icon, medium-font: «044 512 83 91» - Mail icon, medium-font: «ch@torvald-immo.ch» - Website icon, medium-font: « Www.torvald-immo.ch "Very-small-font at bottom of flyer" * The Tippgeberprovision is paid out after the public noti fi cation of the purchase contract as well as after receipt of the mediation commission. The donor commission is 0.2% of the selling price, but the maximum is CHF 3'500 .--. In the event of non-compliance with our mediation commission, payment of the donor commission can not be made. The donor guaranty is only paid once per object and only applies to objects that are not known to us at the time of your contact. We reserve the right to refuse, at our own discretion, any objects, owners or operators. The legal process is excluded. »

Target Market(s)

Every household

Industry/Entity Type

Real Estate

Font styles to use
Serif
Sans Serif

Colors
0255a3
3277b5
33a6d7
85cae6
cfdfed
0692cd

Requirements
Must have
• See project description

```html
<!DOCTYPE html>
<html lang="de">
<head>
<meta charset="utf-8">
<title>Torvald Immobilien – Tippgeber Flyer</title>
<link rel="stylesheet" href="https://fonts.googleapis.com/css2?family=Cinzel:wght@400;700&family=Oswald:wght@600&family=Roboto:wght@300;400&display=swap">
<style>
:root{
  --blue-deep:#0255a3;
  --blue-mid:#3277b5;
  --blue-sky:#33a6d7;
  --blue-light:#85cae6;
  --blue-pale:#cfdfed;
  --blue-bright:#0692cd;
  --ink:#1e1e1e;
  --grey-dark:#4a4b4d;
  --grey-light:#e3e3e3;
  --canvas:#ececec;
}
*{margin:0;padding:0;box-sizing:border-box}
html,body{width:1200px;height:1200px;overflow:hidden;background:var(--canvas)}
.stage{position:relative;width:1200px;height:1200px}
.page{position:absolute;top:243px;width:545px;height:762px;background:#fff;overflow:hidden;box-shadow:0 6px 18px rgba(0,0,0,.18)}
.page--front{left:42px}
.page--back{left:637px}
.abs{position:absolute}

/* front */
.front-shapes{left:0;top:0;width:545px;height:420px}
.brand{left:0;width:545px;top:72px;text-align:center;font-family:'Cinzel',serif;font-weight:700;font-size:22px;letter-spacing:2px;color:var(--ink)}
.front-photo{left:21px;top:111px;width:524px;height:242px;background:linear-gradient(100deg,#dfe3e6 0%,#c9ced3 45%,#8a8e93 75%,#c5cacf 100%)}
.headline{left:0;width:545px;text-align:center}
.headline__big{top:364px;font-family:'Oswald',sans-serif;font-weight:600;font-size:84px;line-height:1;color:var(--blue-deep);letter-spacing:-1px;transform:scaleX(.86)}
.headline__thin{top:455px;font-family:'Roboto',sans-serif;font-weight:300;font-size:62px;line-height:1;color:var(--ink)}
.offer-band{left:0;top:533px;width:545px;height:118px;background:linear-gradient(90deg,#515254 0%,#8c8d8f 50%,#515254 100%);color:#fff;text-align:center}
.offer-band__question{margin-top:14px;font-family:'Cinzel',serif;font-size:21px;line-height:26px;letter-spacing:.3px}
.offer-band__value{margin-top:10px;font-family:'Cinzel',serif;font-weight:700;font-size:21px}
.contact-row{left:0;top:651px;width:545px;height:98px;display:flex;align-items:center}
.contact-row__item{flex:1;text-align:center;font-family:'Cinzel',serif;font-weight:700;font-size:12px;color:var(--ink);height:62px;display:flex;flex-direction:column;align-items:center;justify-content:space-between}
.contact-row__item + .contact-row__item{border-left:1.5px solid var(--ink)}
.footer-bar{left:0;bottom:0;width:545px;height:13px;background:var(--blue-deep)}

/* back */
.back-photo{left:0;top:0;width:545px;height:210px;background:linear-gradient(120deg,#c9cdd3 0%,#eef0f2 40%,#e6c7b2 60%,#f3f4f6 100%)}
.back-accent{left:0;top:0;width:545px;height:340px}
.back-rule{left:0;top:210px;width:545px;height:7px;background:var(--blue-deep)}
.back-title{left:60px;top:238px;font-family:'Cinzel',serif;font-weight:700;font-size:22px;color:var(--ink)}
.back-subtitle{left:60px;top:264px;font-family:'Cinzel',serif;font-weight:400;font-size:21px;color:var(--blue-deep)}
.body-text{font-family:'Roboto',sans-serif;font-size:11.6px;line-height:13.8px;color:var(--ink)}
.intro{left:58px;top:298px;width:413px;text-align:justify}
.section-label{left:58px;font-family:'Cinzel',serif;font-weight:700;font-size:13.5px;color:var(--blue-deep)}
.steps{left:58px;top:396px;width:413px;list-style:none;text-align:left}
.steps li,.address{position:relative;padding-left:29px;margin-bottom:5.5px}
.tick{position:absolute;left:0;top:1px;width:12px;height:12px}
.example{left:58px;top:506px;width:413px;text-align:left}
.address{left:58px;top:543px;width:413px}
.contact-strip{left:0;top:566px;width:545px;height:51px;background:var(--grey-dark);display:flex;justify-content:space-around;align-items:center;padding:0 40px}
.contact-strip__item{text-align:center;font-family:'Cinzel',serif;font-weight:700;font-size:11px;color:#fff;display:flex;flex-direction:column;align-items:center;gap:6px}
.fineprint-area{left:0;top:617px;width:545px;height:134px;background:var(--grey-light)}
.fineprint{left:58px;top:28px;width:433px;font-family:'Roboto',sans-serif;font-size:8.6px;line-height:11.5px;color:#333;text-align:justify}
.back-bottom{left:0;top:751px;width:545px;height:11px;background:var(--blue-deep)}
</style>
</head>
<body>
<div class="stage">

  <section class="page page--front">
    <svg class="abs front-shapes" viewBox="0 0 545 420" aria-hidden="true">
      <rect width="545" height="111" fill="var(--blue-deep)"/>
      <polygon points="0,0 200,0 60,111 0,111" fill="var(--blue-mid)"/>
      <polygon points="330,0 545,0 545,70 420,40" fill="var(--blue-bright)"/>
      <polygon points="420,40 545,70 545,111 470,111" fill="var(--blue-sky)"/>
      <polygon points="60,0 200,0 150,60" fill="var(--blue-sky)" opacity=".55"/>
      <polygon points="0,111 21,111 21,353 0,420" fill="var(--blue-deep)"/>
      <polygon points="0,300 21,280 21,353 0,420" fill="var(--blue-mid)"/>
      <polygon points="272,0 155,111 390,111" fill="#fff"/>
    </svg>
    <div class="abs brand">TORVALD</div>
    <div class="abs front-photo" role="img" aria-label="Foto: drei Geschäftsleute mit einem Bauplan in einem hellen, leeren Büroraum"></div>

    <div class="abs headline headline__big">WIR BEZAHLEN</div>
    <div class="abs headline headline__thin">FÜR IHREN TIPP!</div>

    <div class="abs offer-band">
      <p class="offer-band__question">Sie kennen jemanden, der sein Haus<br>oder seine Wohnung verkaufen will?</p>
      <p class="offer-band__value">Ihr Tipp ist uns bis zu CHF 3'500.- wert!</p>
    </div>

    <div class="abs contact-row">
      <div class="contact-row__item">
        <svg width="26" height="26" viewBox="0 0 24 24" aria-hidden="true"><path fill="var(--blue-deep)" d="M6.6 10.8c1.4 2.8 3.8 5.1 6.6 6.6l2.2-2.2c.3-.3.7-.4 1-.2 1.1.4 2.3.6 3.6.6.6 0 1 .4 1 1V20c0 .6-.4 1-1 1C10.6 21 3 13.4 3 4c0-.6.4-1 1-1h3.5c.6 0 1 .4 1 1 0 1.3.2 2.5.6 3.6.1.3 0 .7-.2 1z"/></svg>
        <span>044 512 83 91</span>
      </div>
      <div class="contact-row__item">
        <svg width="26" height="26" viewBox="0 0 24 24" aria-hidden="true"><circle cx="12" cy="12" r="11" fill="var(--blue-deep)"/><rect x="6" y="7.5" width="12" height="9" rx="1" fill="#fff"/><path d="M6.5 8l5.5 4.5L17.5 8" stroke="var(--blue-deep)" stroke-width="1.4" fill="none"/></svg>
        <span>CH@TORVALD-IMMO.CH</span>
      </div>
      <div class="contact-row__item">
        <svg width="26" height="26" viewBox="0 0 24 24" aria-hidden="true"><circle cx="12" cy="12" r="11" fill="var(--blue-deep)"/><path d="M7 6c2 1 1 3 3 3s1 3-1 3-2 2-1 4M15 5c-1 2 1 3 3 3M14 13c2 0 3 1 3 3s-2 2-2 4" stroke="#fff" stroke-width="2" fill="none" stroke-linecap="round"/></svg>
        <span>WWW.TORVALD-IMMO.CH</span>
      </div>
    </div>
    <div class="abs footer-bar"></div>
  </section>

  <section class="page page--back">
    <div class="abs back-photo" role="img" aria-label="Foto: Händedruck über einem Vertrag mit Schlüsseln auf dem Tisch"></div>
    <svg class="abs back-accent" viewBox="0 0 545 340" aria-hidden="true">
      <polygon points="545,40 495,20 380,150 545,335" fill="var(--blue-mid)" opacity=".8"/>
      <polygon points="545,0 470,0 420,80 545,170" fill="var(--blue-deep)" opacity=".55"/>
      <polygon points="380,150 430,210 545,210 545,335" fill="var(--blue-sky)" opacity=".35"/>
    </svg>
    <div class="abs back-rule"></div>

    <h1 class="abs back-title">Ihr Tipp ist Geld wert!</h1>
    <h2 class="abs back-subtitle">Verraten Sie ihn uns noch heute!</h2>

    <p class="abs body-text intro">Sie kennen in der Familie, im Freundeskreis, im Bekanntenkreis, im Verein oder aus der Berufswelt einen potentiellen Immobilienverkäufer? Ob sofort oder in naher Zukunft kann sich Ihr Tipp für Sie auszahlen. Tippgeber erhalten von uns nach einer erfolgreichen Vermittlung eine Tippgeberprovision von bis zu CHF 3'500.--.*</p>

    <h3 class="abs section-label" style="top:377px">Und so einfach funktionierts:</h3>
    <ul class="abs steps body-text">
      <li><svg class="tick" viewBox="0 0 12 12" aria-hidden="true"><circle cx="6" cy="6" r="5" stroke="var(--blue-deep)" stroke-width="1.3" fill="none"/><path d="M3.5 6l2 2L10 2.5" stroke="var(--blue-deep)" stroke-width="1.5" fill="none"/></svg>Sie kontaktieren uns und geben uns den verkaufswilligen Eigentümer an</li>
      <li><svg class="tick" viewBox="0 0 12 12" aria-hidden="true"><circle cx="6" cy="6" r="5" stroke="var(--blue-deep)" stroke-width="1.3" fill="none"/><path d="M3.5 6l2 2L10 2.5" stroke="var(--blue-deep)" stroke-width="1.5" fill="none"/></svg>Wir kontaktieren den Eigentümer und schliessen einen Maklervertrag ab</li>
      <li><svg class="tick" viewBox="0 0 12 12" aria-hidden="true"><circle cx="6" cy="6" r="5" stroke="var(--blue-deep)" stroke-width="1.3" fill="none"/><path d="M3.5 6l2 2L10 2.5" stroke="var(--blue-deep)" stroke-width="1.5" fill="none"/></svg>Wir starten den Verkaufsprozess und informieren Sie über die Fortschritte</li>
      <li><svg class="tick" viewBox="0 0 12 12" aria-hidden="true"><circle cx="6" cy="6" r="5" stroke="var(--blue-deep)" stroke-width="1.3" fill="none"/><path d="M3.5 6l2 2L10 2.5" stroke="var(--blue-deep)" stroke-width="1.5" fill="none"/></svg>Nach erfolgreichem Verkaufsabschluss erhalten Sie Ihre Tippgeberprovision!</li>
    </ul>

    <h3 class="abs section-label" style="top:490px">Beispiel:</h3>
    <p class="abs body-text example">Dank Ihrem Tipp können wir eine Immobilie zu 1.5 Mio verkaufen. Ihre Tippgeberprovision beträgt in dem Fall CHF 3'000.-- (0.2% von CHF 1'500'000.--)</p>
    <p class="abs body-text address"><svg class="tick" viewBox="0 0 12 12" aria-hidden="true"><circle cx="6" cy="6" r="5" stroke="var(--blue-deep)" stroke-width="1.3" fill="none"/><path d="M3.5 6l2 2L10 2.5" stroke="var(--blue-deep)" stroke-width="1.5" fill="none"/></svg>"Torvald Immobilien + Treuhand AG Almweg 14 6331 Hünenberg"</p>

    <div class="abs contact-strip">
      <div class="contact-strip__item">
        <svg width="20" height="20" viewBox="0 0 24 24" aria-hidden="true"><path fill="#fff" d="M6.6 10.8c1.4 2.8 3.8 5.1 6.6 6.6l2.2-2.2c.3-.3.7-.4 1-.2 1.1.4 2.3.6 3.6.6.6 0 1 .4 1 1V20c0 .6-.4 1-1 1C10.6 21 3 13.4 3 4c0-.6.4-1 1-1h3.5c.6 0 1 .4 1 1 0 1.3.2 2.5.6 3.6.1.3 0 .7-.2 1z"/></svg>
        <span>044 512 83 91</span>
      </div>
      <div class="contact-strip__item">
        <svg width="20" height="20" viewBox="0 0 24 24" aria-hidden="true"><circle cx="12" cy="12" r="11" fill="#fff"/><rect x="6" y="7.5" width="12" height="9" rx="1" fill="none" stroke="var(--grey-dark)" stroke-width="1.4"/><path d="M6.5 8l5.5 4.5L17.5 8" stroke="var(--grey-dark)" stroke-width="1.4" fill="none"/></svg>
        <span>CH@TORVALD-IMMO.CH</span>
      </div>
      <div class="contact-strip__item">
        <svg width="20" height="20" viewBox="0 0 24 24" aria-hidden="true"><circle cx="12" cy="12" r="11" fill="#fff"/><path d="M7 6c2 1 1 3 3 3s1 3-1 3-2 2-1 4M15 5c-1 2 1 3 3 3M14 13c2 0 3 1 3 3s-2 2-2 4" stroke="var(--grey-dark)" stroke-width="2" fill="none" stroke-linecap="round"/></svg>
        <span>WWW.TORVALD-IMMO.CH</span>
      </div>
    </div>

    <div class="abs fineprint-area">
      <p class="abs fineprint">*Die Tippgeberprovision wird nach der öffentlichen Beurkundung des Kaufvertrags sowie nach Erhalt der Vermittlungsprovision ausbezahlt. Die Tippgeberprovision beträgt 0.2% des erzielten Verkaufspreises, im Maximum jedoch CHF 3'500.--. Bei Nichterhalt unserer Vermittlungsprovision kann auch keine Auszahlung der Tippgeberprovision erfolgen. Die Tippgeberprovision wird pro Objekt nur einmalig ausbezahlt und gilt nur für Objekte, die uns zum Zeitpunkt Ihrer Kontaktaufnahme noch nicht bekannt sind. Wir behalten uns das Recht vor nach eigenem Ermessen Objekte, Eigentümer oder Tippgeber abzulehnen. Der Rechtsweg ist ausgeschlossen.</p>
    </div>
    <div class="abs back-bottom"></div>
  </section>

</div>
</body>
</html>
```